Looking for a modern, Professional business card design

We have a simple business card, but are looking for a more modern, professional look. A sample of the basic card is attached as well as the logo. We would also like to add that we offer:
Struggling with your finances?
- Learn to become debt free
- Discover the power of cash
- Control your money instead of it controlling you
Let us help you achieve a new level of financial freedom!
Also, we would like to have a "SPECIAL OFFER!: FREE 30 minute consultation"
Financial Planning

```html
<!DOCTYPE html>
<html lang="en">
<head>
<meta charset="utf-8">
<title>Summit Financial Coaching – Business Card</title>
<link rel="stylesheet" href="https://fonts.googleapis.com/css2?family=Libre+Franklin:wght@400;600;800;900&display=swap">
<style>
  :root {
    --backdrop: #e6e6e6;
    --card-black: #050505;
    --brand-green: #2b8a3e;
    --brand-green-bright: #3fa33a;
    --offer-green: #4a9e2c;
    --paper: #f4f4f4;
    --ink: #111111;
    --ink-soft: #3a3a3a;
    --white: #ffffff;
  }
  * { box-sizing: border-box; margin: 0; padding: 0; }
  html, body {
    width: 1105px; height: 1200px; overflow: hidden;
    background: var(--backdrop);
    font-family: "Libre Franklin", Arial, sans-serif;
  }
  .canvas { position: relative; width: 1105px; height: 1200px; }
  .card {
    position: absolute; left: 182px; width: 746px; height: 426px; overflow: hidden;
  }

  /* Front */
  .card--front { top: 119px; background: var(--card-black); }
  .front-field { position: absolute; inset: 0; }
  .contact-block {
    position: absolute; right: 72px; top: 196px; text-align: right; color: var(--white);
  }
  .holder-name {
    color: var(--brand-green-bright); font-size: 29px; font-weight: 400; letter-spacing: 0.5px;
    line-height: 1; margin-right: 22px;
  }
  .holder-role { font-size: 20px; margin-top: 12px; margin-right: 22px; }
  .contact-list { list-style: none; margin-top: 26px; }
  .contact-item {
    display: flex; justify-content: flex-end; align-items: center; gap: 12px;
    font-size: 19px; line-height: 29px;
  }
  .contact-item svg { width: 18px; height: 18px; fill: var(--brand-green-bright); flex: none; }

  /* Back */
  .card--back { top: 637px; background: var(--paper); text-align: center; }
  .brand-lockup {
    position: absolute; top: 70px; left: 0; right: 0;
    display: flex; justify-content: center; align-items: center; gap: 14px;
  }
  .brand-dot { width: 26px; height: 26px; border-radius: 50%; background: var(--brand-green-bright); }
  .brand-name { font-size: 40px; font-weight: 800; color: var(--ink); letter-spacing: 0.5px; }
  .brand-tagline {
    position: absolute; top: 128px; left: 0; right: 0;
    font-size: 13px; color: var(--ink-soft);
  }
  .pitch { position: absolute; top: 245px; left: 0; right: 0; }
  .pitch-heading { color: var(--brand-green); font-size: 21px; font-weight: 600; }
  .pitch-points { color: var(--ink-soft); font-size: 20px; line-height: 27px; margin-top: 4px; }
  .bullet { color: var(--brand-green-bright); }
  .pitch-close { color: var(--ink); font-size: 20px; font-weight: 600; margin-top: 8px; }
  .special-offer {
    color: var(--offer-green); font-size: 26px; font-weight: 900; margin-top: 10px; letter-spacing: 0.2px;
  }
</style>
</head>
<body>
<main class="canvas">
  <section class="card card--front" aria-label="Card front">
    <svg class="front-field" viewBox="0 0 746 426" aria-hidden="true">
      <path d="M0 0 H530 Q300 120 170 426 H0 Z" fill="var(--brand-green)"/>
    </svg>
    <div class="contact-block">
      <h1 class="holder-name">DANIEL R. HAYES</h1>
      <p class="holder-role">Personal Financial Coach</p>
      <ul class="contact-list">
        <li class="contact-item">(205) 555-0148
          <svg viewBox="0 0 18 18"><path d="M5 0h8a2 2 0 0 1 2 2v14a2 2 0 0 1-2 2H5a2 2 0 0 1-2-2V2a2 2 0 0 1 2-2zm0 2v12h8V2zm4 13.2a.9.9 0 1 0 0 1.8.9.9 0 0 0 0-1.8z"/></svg>
        </li>
        <li class="contact-item">daniel@steadyledgercoach.com
          <svg viewBox="0 0 18 18"><path d="M1 4h16v11H1zm1.5 1.2L9 10l6.5-4.8V5.2z"/></svg>
        </li>
        <li class="contact-item">www.steadyledgercoach.com
          <svg viewBox="0 0 18 18"><circle cx="9" cy="9" r="8"/><path d="M5 6c2 0 2 2 4 2s1 3 3 3M10 3c1 2 4 1 4 4" stroke="var(--card-black)" stroke-width="1.4" fill="none"/></svg>
        </li>
      </ul>
    </div>
  </section>

  <section class="card card--back" aria-label="Card back">
    <div class="brand-lockup">
      <span class="brand-dot" aria-hidden="true"></span>
      <span class="brand-name">Summit Financial Coaching</span>
    </div>
    <p class="brand-tagline">Achieve a new level of personal freedom</p>
    <div class="pitch">
      <h2 class="pitch-heading">STRUGGLING WITH YOUR FINANCES?</h2>
      <p class="pitch-points">Learn to become debt free<span class="bullet">&#9679;</span> Discover the power of cash<br>Control your money instead of it controlling you</p>
      <p class="pitch-close">Let us help you achieve a new level of financial freedom!</p>
      <p class="special-offer">SPECIAL OFFER!: FREE 30 minute consultation</p>
    </div>
  </section>
</main>
</body>
</html>
```